New emergency medical service needs a marketing flyer for prospective customers

We need a tri fold brochure on an 8.5 X 11 stock for a new emergency medical service in Pennsylvania. We provide basic first aid and now Covid-19 pre screening and temperature monitoring for special events, large gatherings and businesses. Examples of these would be but not limited to: Sporting events, carnivals, festivals, craft shows, warehouses, churches, manufacturing facilities, industrial buildings, large construction sites, multi occupancy officer buildings. The market for this is pretty much untouched and endless. we would like to use gray as the back ground color and obviously our logo. The final design should grab their attention and communicate the importance of having trained and certified professionals at their event or facility. We want to give them that piece of mind they are in good hands with us.

Target Market(s)

primary focus is going to be on businesses with large offices, large buildings or lots of foot traffic in and out of the building

Requirements
Must have
• gray background, pictures, company phone # , company web site, and contact email address. I will provide all that information to the winner to add at the end.
Nice to have
• pictures that covers the whole front cover with logo at top

```html
<!DOCTYPE html>
<html lang="en">
<head>
<meta charset="utf-8">
<title>Keystone Care Medical Services – Tri-fold Brochure</title>
<link href="https://fonts.googleapis.com/css2?family=Montserrat:wght@600;700;800&family=Open+Sans:wght@400;600&display=swap" rel="stylesheet">
<style>
  :root {
    --bg: #4b5057;
    --purple: #2f2f9c;
    --purple-deep: #25247f;
    --purple-light: #4545c4;
    --dark: #2a2a2d;
    --teal: #1fb39a;
    --white: #ffffff;
    --paper: #f4f5f7;
    --photo-cool: #c9d3de;
    --photo-blue: #6f8fb8;
    --ink-soft: #d9dbf5;
  }
  * { box-sizing: border-box; margin: 0; padding: 0; }
  html, body { width: 1200px; height: 1200px; overflow: hidden; }
  body {
    background: var(--bg);
    font-family: "Open Sans", Arial, sans-serif;
    display: flex; flex-direction: column; align-items: center;
    gap: 16px; padding-top: 18px;
  }
  .sheet {
    width: 740px; height: 572px; display: flex;
    background: var(--paper);
    box-shadow: 0 10px 30px rgba(0,0,0,.35);
  }
  .panel { position: relative; width: 33.333%; height: 100%; overflow: hidden; }
  .panel + .panel { border-left: 1px solid rgba(0,0,0,.12); }
  .photo { position: absolute; left: 0; right: 0; }
  .photo-cool { background: linear-gradient(160deg, #e7ecf2 0%, var(--photo-cool) 45%, var(--photo-blue) 100%); }
  .photo-warm { background: linear-gradient(170deg, #dfe4ea 0%, #aeb8c6 55%, #7d8aa3 100%); }
  .block { position: absolute; left: 0; right: 0; }
  .purple { background: linear-gradient(160deg, var(--purple-light) 0%, var(--purple) 50%, var(--purple-deep) 100%); color: var(--white); }
  .dark { background: var(--dark); color: var(--white); }
  h2.section-title {
    font-family: "Montserrat", Arial, sans-serif; font-weight: 700;
    font-size: 14px; letter-spacing: .5px; text-transform: uppercase;
    display: flex; align-items: center; gap: 8px;
  }
  .dark h2.section-title, .purple h2.teal-title { color: var(--teal); }
  .mark { width: 14px; height: 14px; background: var(--white); border-radius: 50%; flex: none; }
  .body-copy { font-size: 7.6px; line-height: 1.45; color: var(--ink-soft); text-align: justify; }
  .dark .body-copy { color: #e6e6e6; }
  .subhead { font-family: "Montserrat", Arial, sans-serif; font-weight: 600; font-size: 10.5px; color: var(--teal); margin: 10px 0 4px; }
  .web-strip {
    position: absolute; left: 0; right: 0; font-size: 8px; letter-spacing: 2px;
    font-family: "Montserrat", Arial, sans-serif; font-weight: 600; text-align: center;
  }
  .teal-band { background: var(--teal); color: var(--white); padding: 5px 0; }
  .brand-name { font-family: "Montserrat", Arial, sans-serif; font-weight: 800; display: flex; align-items: center; gap: 8px; line-height: 1.05; }
  .brand-dot { width: 16px; height: 16px; background: var(--teal); border-radius: 50%; flex: none; }
  .contact-list { list-style: none; font-size: 8.5px; text-align: center; }
  .contact-list li { display: flex; flex-direction: column; align-items: center; gap: 3px; margin-bottom: 10px; }
  .icon { width: 12px; height: 12px; border-radius: 50%; background: var(--teal); display: flex; align-items: center; justify-content: center; }
  .ticks { list-style: none; }
  .ticks li { display: flex; gap: 10px; align-items: center; margin-bottom: 11px; }
  .tick { width: 22px; height: 22px; border-radius: 50%; background: var(--teal); flex: none; display: flex; align-items: center; justify-content: center; }
  .ticks p { font-size: 7.6px; line-height: 1.4; color: #e6e6e6; }
</style>
</head>
<body>

<!-- Outside of the brochure -->
<section class="sheet sheet-outside">
  <article class="panel panel-about">
    <div class="photo photo-cool" style="top:0;height:170px" role="img" aria-label="Photo of a surgeon in cap and mask"></div>
    <div class="block purple" style="top:150px;height:350px;border-radius:0 40px 0 0;padding:28px 22px 0">
      <h2 class="section-title"><span class="mark"></span>About Us</h2>
      <p class="body-copy" style="margin-top:14px">Lorem ipsum dolor sit amet, consectetur adipiscing elit, sed do eiusmod tempor incididunt ut labore et dolore magna aliqua. Ut enim ad minim veniam, quis nostrud exercitation ullamco laboris nisi ut aliquip ex ea commodo consequat. Duis aute irure dolor in reprehenderit in voluptate velit esse cillum dolore eu fugiat nulla pariatur sint occaecat cupidatat non proident.</p>
      <p class="body-copy" style="margin-top:8px">Tristique risus nec feugiat in fermentum posuere. Habitasse platea dictumst quisque sagittis purus sit amet volutpat. Velit aliquet sagittis id consectetur purus ut faucibus pulvinar. Metus dictum at tempor commodo ullamcorper a lacus vestibulum sed. Consectetur a erat nam at lectus urna duis.</p>
    </div>
    <div class="block dark" style="top:500px;height:72px"></div>
    <div class="web-strip" style="top:526px;color:var(--teal)">www.keystonecare.example</div>
  </article>

  <article class="panel panel-contact">
    <div class="photo photo-cool" style="top:0;height:190px" role="img" aria-label="Photo of a nurse at hospital monitoring equipment"></div>
    <div class="block purple" style="top:170px;height:310px;border-radius:40px 0 0 40px;padding:50px 18px 0;display:flex;flex-direction:column;align-items:center">
      <div class="brand-name" style="font-size:16px;color:var(--white)"><span class="brand-dot"></span>Keystone Care</div>
      <h2 class="section-title" style="margin-top:30px;font-size:12px;text-transform:none">Contact Us</h2>
      <ul class="contact-list" style="margin-top:16px">
        <li><span class="icon"><svg width="7" height="7" viewBox="0 0 10 10"><path d="M2 1l2 2-1 1.2a6 6 0 0 0 2.8 2.8L7 6l2 2-1.2 1.5C4.5 9.5.5 5.5.5 2.2z" fill="#fff"/></svg></span>(+012) 555 0148</li>
        <li><span class="icon"><svg width="7" height="6" viewBox="0 0 10 8"><rect x=".5" y=".5" width="9" height="7" fill="#fff"/><path d="M.5.5l4.5 4 4.5-4" stroke="#1fb39a" fill="none"/></svg></span>info@keystonecare.example</li>
        <li><span class="icon"><svg width="7" height="7" viewBox="0 0 10 10"><circle cx="5" cy="5" r="4" stroke="#fff" fill="none"/><path d="M1 5h8M5 1c-2 2.5-2 5.5 0 8M5 1c2 2.5 2 5.5 0 8" stroke="#fff" fill="none" stroke-width=".8"/></svg></span>www.keystonecare.example</li>
      </ul>
    </div>
    <div class="photo photo-warm" style="top:480px;height:92px;z-index:-0" role="img" aria-label="Photo of a stethoscope"></div>
  </article>

  <article class="panel panel-cover">
    <div class="block" style="top:0;height:200px;background:var(--white);display:flex;align-items:center;justify-content:center">
      <div class="brand-name" style="font-size:22px;color:var(--purple);flex-direction:row">
        <span class="brand-dot" style="width:22px;height:22px"></span>
        <span>Keystone Care<br><span style="font-size:11px">Medical Services</span></span>
      </div>
    </div>
    <div class="photo photo-cool" style="top:200px;bottom:0;border-top:2px solid var(--teal);border-radius:40px 0 0 0" role="img" aria-label="Photo of a masked medic in scrubs holding a clipboard"></div>
    <div class="web-strip teal-band" style="top:520px;left:14px;right:14px">www.keystonecare.example</div>
  </article>
</section>

<!-- Inside of the brochure -->
<section class="sheet sheet-inside">
  <article class="panel panel-intro">
    <div class="photo photo-cool" style="top:0;height:230px" role="img" aria-label="Photo of gloved medic handling a stethoscope"></div>
    <div class="block dark" style="top:215px;height:320px;padding:22px 20px 0;border-radius:0 30px 0 0">
      <h2 class="section-title"><span class="mark"></span>Lorem ipsum dolor<br>sit amet</h2>
      <p class="body-copy" style="margin-top:8px">Lorem ipsum dolor sit amet, consectetur adipiscing elit, sed do eiusmod tempor incididunt ut labore et dolore magna aliqua.</p>
      <h3 class="subhead">Lorem ipsum dolor</h3>
      <p class="body-copy">Ut enim ad minim veniam, quis nostrud exercitation ullamco laboris nisi ut aliquip ex ea commodo consequat. Duis aute irure dolor in reprehenderit in voluptate velit esse cillum dolore eu fugiat nulla pariatur. Excepteur sint occaecat cupidatat non proident, sunt in culpa qui officia deserunt mollit anim id est laborum.</p>
      <h3 class="subhead">Lorem ipsum dolor</h3>
      <p class="body-copy">Tristique risus nec feugiat in fermentum posuere. Habitasse platea dictumst quisque sagittis purus sit amet volutpat. Velit aliquet sagittis id consectetur purus ut faucibus pulvinar. Metus dictum at tempor commodo ullamcorper a lacus vestibulum sed.</p>
    </div>
    <div class="block" style="top:548px;height:2px;background:var(--teal)"></div>
  </article>

  <article class="panel panel-list">
    <div class="photo photo-cool" style="top:0;height:160px" role="img" aria-label="Photo of gloved hand filling in a test form"></div>
    <div class="block dark" style="top:140px;height:335px;padding:20px 18px 0;border-radius:30px 0 0 0">
      <h2 class="section-title" style="margin-bottom:14px"><span class="mark"></span>Lorem ipsum dolor</h2>
      <ul class="ticks">
        <li><span class="tick"><svg width="11" height="9" viewBox="0 0 11 9"><path d="M1 4.5l3 3L10 1" stroke="#fff" stroke-width="2" fill="none"/></svg></span><p>Lorem ipsum dolor sit amet. Odio aenean sed adipiscing diam donec adipiscing tristique risus nec.</p></li>
        <li><span class="tick"><svg width="11" height="9" viewBox="0 0 11 9"><path d="M1 4.5l3 3L10 1" stroke="#fff" stroke-width="2" fill="none"/></svg></span><p>Lorem ipsum dolor sit amet. Odio aenean sed adipiscing diam donec adipiscing tristique risus nec.</p></li>
        <li><span class="tick"><svg width="11" height="9" viewBox="0 0 11 9"><path d="M1 4.5l3 3L10 1" stroke="#fff" stroke-width="2" fill="none"/></svg></span><p>Lorem ipsum dolor sit amet. Odio aenean sed adipiscing diam donec adipiscing tristique risus nec.</p></li>
        <li><span class="tick"><svg width="11" height="9" viewBox="0 0 11 9"><path d="M1 4.5l3 3L10 1" stroke="#fff" stroke-width="2" fill="none"/></svg></span><p>Lorem ipsum dolor sit amet. Odio aenean sed adipiscing diam donec adipiscing tristique risus nec. Quam nulla porttitor massa id neque elementum.</p></li>
        <li><span class="tick"><svg width="11" height="9" viewBox="0 0 11 9"><path d="M1 4.5l3 3L10 1" stroke="#fff" stroke-width="2" fill="none"/></svg></span><p>Lorem ipsum dolor sit amet. Odio aenean sed adipiscing diam donec adipiscing tristique risus nec.</p></li>
      </ul>
    </div>
    <div class="web-strip teal-band" style="top:505px;left:22px;right:22px">www.keystonecare.example</div>
  </article>

  <article class="panel panel-services">
    <div class="photo" style="top:0;height:230px;background:linear-gradient(180deg,#d8dde4 0%,#9aa6c4 55%,var(--purple-light) 100%)" role="img" aria-label="Photo of medics in protective suits moving a patient"></div>
    <div class="block purple" style="top:215px;bottom:0;padding:4px 18px 0;background:linear-gradient(180deg,var(--purple-light) 0%,var(--purple) 40%,var(--purple-deep) 100%)">
      <h2 class="section-title teal-title"><span class="mark"></span>Lorem ipsum dolor</h2>
      <h3 class="subhead">Lorem ipsum dolor</h3>
      <p class="body-copy">Ut enim ad minim veniam, quis nostrud exercitation ullamco laboris nisi ut aliquip ex ea commodo consequat. Duis aute irure dolor in reprehenderit in voluptate velit esse cillum dolore eu fugiat nulla pariatur. Excepteur sint occaecat cupidatat non proident, sunt in culpa qui officia deserunt mollit anim id est laborum.</p>
      <p class="body-copy" style="margin-top:6px">At imperdiet dui accumsan sit. Lorem sed risus ultricies tristique nulla aliquet enim tortor at. Diam phasellus vestibulum lorem sed risus ultricies tristique nulla aliquet. Massa eget egestas purus viverra accumsan in nisl. Risus quis varius quam quisque.</p>
      <div class="brand-name" style="font-size:15px;color:var(--white);margin-top:22px"><span class="brand-dot"></span>Keystone Care</div>
      <p style="font-family:'Montserrat',Arial,sans-serif;font-weight:700;font-size:15px;margin-top:8px">(+012) 555 0148</p>
      <p style="font-size:8.5px;margin-top:4px">info@keystonecare.example</p>
      <p style="font-size:8.5px;margin-top:2px">www.keystonecare.example</p>
    </div>
  </article>
</section>

</body>
</html>
```